custom carpentry, woodworking and home repair company needs logo design and business card design

Attention: I apologize but I just received notification from my state that I cannot use the company name that I originally submitted (Beyond The Bench). The new name will be Joinolux We need a company logo and business card design for our new company based in the Hampton Roads area of Virginia. The company name is Joinolux. The final design should give a first impression of true craftsmanship and attention to detail. We would like the card to include the company name, my name Mark Tellman (owner), phone number (757) 348-2615, website (joinolux-example.com) and email address (mark@joinolux-example.com). Everything else is up to your discretion. Thanks, have fun, and good luck.

Industry/Entity Type

Business

Contact Information for Business Card

See project description

Logo Text

see project description

Colors

Designer to choose colors to be used in the design.

```html
<!DOCTYPE html>
<html lang="en">
<head>
<meta charset="UTF-8">
<title>Joinolux Business Card</title>
<link href="https://fonts.googleapis.com/css2?family=Lato:wght@400;700;900&display=swap" rel="stylesheet">
<style>
  :root {
    --navy: #33475f;
    --navy-ink: #2c3e57;
    --tan: #b39b7a;
    --white: #ffffff;
    --backdrop: #2a2a2b;
    --rule: #4a5a70;
  }
  * { margin: 0; padding: 0; box-sizing: border-box; }
  html, body {
    width: 1200px; height: 880px; overflow: hidden;
    background: var(--backdrop);
    font-family: "Lato", Arial, sans-serif;
  }
  .stage { position: relative; width: 1200px; height: 880px; }
  .card {
    position: absolute;
    width: 620px; height: 354px;
    border-radius: 22px;
  }
  .card-front {
    left: 120px; top: 70px;
    background: var(--navy);
    display: flex; align-items: center; justify-content: center;
  }
  .card-back {
    left: 460px; top: 456px;
    background: var(--white);
  }
  .brand {
    display: flex; align-items: center; gap: 14px;
    font-weight: 900; font-size: 40px; letter-spacing: 3px;
    text-transform: uppercase;
  }
  .brand-dot {
    width: 30px; height: 30px; border-radius: 50%;
  }
  .card-front .brand { color: var(--white); }
  .card-front .brand-dot { background: var(--white); }
  .card-back .brand {
    position: absolute; left: 44px; top: 152px;
    color: var(--navy-ink); font-size: 34px; gap: 12px;
  }
  .card-back .brand-dot { background: var(--tan); width: 26px; height: 26px; }
  .divider {
    position: absolute; left: 330px; top: 92px;
    width: 1px; height: 170px; background: var(--rule);
  }
  .contact {
    position: absolute; left: 368px; top: 96px;
  }
  .person-name {
    font-weight: 700; font-size: 25px; color: var(--navy-ink); line-height: 1.05;
  }
  .person-role {
    font-size: 18px; color: var(--tan); line-height: 1.1;
  }
  .contact-list { list-style: none; margin-top: 40px; }
  .contact-item {
    display: flex; align-items: center; gap: 9px;
    font-size: 16px; color: var(--navy-ink); line-height: 1; margin-bottom: 7px;
  }
  .contact-icon { width: 20px; height: 20px; flex: none; }
</style>
</head>
<body>
<main class="stage">
  <section class="card card-front">
    <div class="brand"><span class="brand-dot"></span>Joinolux</div>
  </section>

  <section class="card card-back">
    <div class="brand"><span class="brand-dot"></span>Joinolux</div>
    <div class="divider"></div>
    <div class="contact">
      <p class="person-name">Mark Tellman</p>
      <p class="person-role">Owner</p>
      <ul class="contact-list">
        <li class="contact-item">
          <svg class="contact-icon" viewBox="0 0 20 20"><circle cx="10" cy="10" r="10" fill="#b39b7a"/><path d="M7 5.5l1.6 2.4-1 1.1c.7 1.4 1.6 2.3 3 3l1.1-1 2.4 1.6-.9 1.7c-3.6-.5-6.4-3.3-6.9-6.9z" fill="#fff"/></svg>
          (757) 348-2615
        </li>
        <li class="contact-item">
          <svg class="contact-icon" viewBox="0 0 20 20"><circle cx="10" cy="10" r="10" fill="#b39b7a"/><rect x="5" y="6.5" width="10" height="7" rx="1" fill="#fff"/><path d="M5.5 7l4.5 3.5L14.5 7" stroke="#b39b7a" stroke-width="1" fill="none"/></svg>
          mark@joinolux-example.com
        </li>
        <li class="contact-item">
          <svg class="contact-icon" viewBox="0 0 20 20"><circle cx="10" cy="10" r="10" fill="#b39b7a"/><circle cx="10" cy="10" r="5" fill="none" stroke="#fff" stroke-width="1.2"/><path d="M5 10h10M10 5c-2 3-2 7 0 10M10 5c2 3 2 7 0 10" stroke="#fff" stroke-width="1" fill="none"/></svg>
          joinolux-example.com
        </li>
      </ul>
    </div>
  </section>
</main>
</body>
</html>
```